Business Card Design Project

KV Strategy Partners is a management consulting business with C-suite (CEO/CFO etc) target clients. Logo selected is blue with simple/serious typefaces.

Target Market(s)

CEOs and CFOs of large corporates

Industry/Entity Type

Management Consulting

Font styles to use
Serif

Colors
3276b5

Requirements
Must have
• Tag line: Building successful collaborations (use different font)
Address: 457 Cedar Brook Lane #03-22 Singapore 519307
Telephone: +65 8372 6094
Email: kvlorne@mailbox47.com

```html
<!DOCTYPE html>
<html lang="en">
<head>
<meta charset="utf-8">
<title>KV Strategy Partners – Business Card</title>
<link rel="stylesheet" href="https://fonts.googleapis.com/css2?family=Cinzel:wght@400&family=Cormorant+Garamond:ital,wght@1,500&family=Lora:wght@400&display=swap">
<style>
  :root {
    --card-top: #213a4c;
    --card-band: #2a4f68;
    --ink: #ffffff;
    --ink-soft: #e8eef3;
  }
  * { margin: 0; padding: 0; box-sizing: border-box; }
  html, body { width: 1200px; height: 720px; overflow: hidden; background: var(--card-top); }
  .card { position: relative; width: 1200px; height: 720px; background: var(--card-top); color: var(--ink); }
  .brand-square {
    position: absolute; left: 530px; top: 218px; width: 135px; height: 135px;
    background: var(--ink); border-radius: 10px;
  }
  .brand-name {
    position: absolute; left: 0; right: 0; top: 364px; text-align: center;
    font-family: "Cinzel", serif; font-weight: 400; font-size: 54px;
    letter-spacing: 2px; text-transform: uppercase; line-height: 1;
  }
  .tagline {
    position: absolute; left: 0; right: 0; top: 424px; text-align: center;
    font-family: "Cormorant Garamond", serif; font-style: italic; font-weight: 500;
    font-size: 26px; letter-spacing: 1.5px; color: var(--ink-soft); line-height: 1.2;
  }
  .contact-band {
    position: absolute; left: 0; top: 530px; width: 1200px; height: 190px;
    background: var(--card-band);
  }
  .contact-item {
    position: absolute;
    font-family: "Lora", serif; font-size: 22px; color: var(--ink); line-height: 24px;
  }
  .contact-item svg { position: absolute; width: 24px; height: 24px; fill: var(--ink); }
  .contact-text { position: absolute; white-space: nowrap; }
</style>
</head>
<body>
<main class="card">
  <div class="brand-square" aria-hidden="true"></div>
  <h1 class="brand-name">KV Strategy Partners</h1>
  <p class="tagline">Building successful collaborations</p>

  <section class="contact-band" aria-label="Contact details">
    <div class="contact-item" style="left:76px;top:66px;">
      <svg viewBox="0 0 24 24" style="left:0;top:0"><path d="M12 1a8 8 0 0 0-8 8c0 6 8 14 8 14s8-8 8-14a8 8 0 0 0-8-8zm0 11a3 3 0 1 1 0-6 3 3 0 0 1 0 6z"/></svg>
      <span class="contact-text" style="left:38px;top:0">457 Cedar Brook Lane</span>
      <span class="contact-text" style="left:38px;top:45px">#03-22 Singapore 519307</span>
    </div>

    <div class="contact-item" style="left:458px;top:66px;">
      <svg viewBox="0 0 24 24" style="left:0;top:0"><path d="M6.6 10.8c1.4 2.8 3.8 5.1 6.6 6.6l2.2-2.2c.3-.3.7-.4 1-.2 1.1.4 2.3.6 3.6.6.6 0 1 .4 1 1V20c0 .6-.4 1-1 1C10.6 21 3 13.4 3 4c0-.6.4-1 1-1h3.5c.6 0 1 .4 1 1 0 1.3.2 2.5.6 3.6.1.3 0 .7-.2 1z"/></svg>
      <span class="contact-text" style="left:49px;top:0">+65 8372 6094</span>
    </div>
    <div class="contact-item" style="left:458px;top:111px;">
      <svg viewBox="0 0 24 24" style="left:0;top:0"><path d="M6 2h10v7H6zM8 4v3h6V4zM3 10h18v9H3zm3 3v2h12v-2zM5 20h14v2H5z"/></svg>
      <span class="contact-text" style="left:49px;top:0">+65 8372 6095</span>
    </div>

    <div class="contact-item" style="left:820px;top:66px;">
      <svg viewBox="0 0 24 24" style="left:0;top:0"><path d="M12 1a11 11 0 1 0 0 22 11 11 0 0 0 0-22zm-2 4c2 1 1 3 3 3s2 2 0 3-4 0-5 2 1 4-1 5c-2-1-3-4-3-6 0-4 3-7 6-7zm6 9c2 0 3 1 2 3-1 1-3 2-4 1 0-2 1-4 2-4z"/></svg>
      <span class="contact-text" style="left:49px;top:0">www.kvstrategy.com</span>
    </div>
    <div class="contact-item" style="left:820px;top:111px;">
      <svg viewBox="0 0 24 24" style="left:0;top:0"><path d="M2 5h20v14H2zm2 2v1l8 6 8-6V7zm0 3.5V17h16v-6.5l-8 6z"/></svg>
      <span class="contact-text" style="left:49px;top:0">kvlorne@mailbox47.com</span>
    </div>
  </section>
</main>
</body>
</html>
```